Tillard Environmental Projects New Website Design

I need a new website for a Environmental Project Company based in Sydney Australia, working throughout South East Asia.I've attached the company logo, please try & incorporate these colours or use complimentary colours. I've attached a word doc with design brief.I'm going to use Wix, so please ensure files are suitable.Thankyou.

Number of Pages Required

5+ page

Colors

Designer to choose colors to be used in the design.

Requirements
Must have
• Refer to Word Document
Nice to have
• Refer to Word Document
Should not have
• Not to be dark

```html
<!DOCTYPE html>
<html lang="en">
<head>
<meta charset="utf-8">
<title>Tillard Environmental Projects</title>
<link href="https://fonts.googleapis.com/css2?family=Poppins:ital,wght@0,400;0,500;0,600;0,700;1,400&display=swap" rel="stylesheet">
<style>
:root{
  --green-dark:#3b5a16;
  --green-deep:#1f4d0e;
  --green-mid:#5f9b1e;
  --green-lime:#a8d62e;
  --green-pale:#d4ec8a;
  --text:#222;
  --muted:#555;
  --grey-bg:#f4f5f7;
  --line:#ddd;
  --white:#fff;
}
*{margin:0;padding:0;box-sizing:border-box}
html,body{width:1200px;height:2659px;overflow:hidden;background:var(--white)}
body{font-family:"Poppins",sans-serif;color:var(--text);position:relative}
.abs{position:absolute}
/* header */
.site-header{position:absolute;left:0;top:0;width:1200px;height:92px;z-index:3}
.brand{position:absolute;left:64px;top:22px;display:flex;align-items:center;gap:12px}
.brand-dot{width:44px;height:44px;border-radius:50%;background:var(--green-dark)}
.brand-name{font-size:15px;font-weight:600;color:var(--green-dark);line-height:1.15;width:150px}
.main-nav{position:absolute;left:418px;top:38px;display:flex;gap:20px;font-size:12px;color:#333}
.main-nav span.drop::after{content:"";display:inline-block;margin-left:4px;border:3px solid transparent;border-top-color:#555;vertical-align:1px}
.search{position:absolute;left:950px;top:32px;width:188px;height:30px;background:var(--white);border:1px solid var(--line);font-size:10px;color:#777;padding:8px 10px}
.search svg{position:absolute;right:9px;top:7px}
/* hero */
.hero{position:absolute;left:0;top:92px;width:1200px;height:490px;background:var(--grey-bg);overflow:hidden}
.hero-art{position:absolute;left:330px;top:20px;width:540px;height:440px;border-radius:50%;background:radial-gradient(circle,#e6ebe1 0%,#eef0ec 60%,rgba(243,244,246,0) 75%)}
.hero-accent-left{position:absolute;left:0;top:150px;width:470px;height:340px;background:linear-gradient(to top right,#3f7a14 0%,#6aa82a 24%,#a8d62e 44%,rgba(212,236,138,0) 62%)}
.hero-accent-right{position:absolute;right:0;top:0;width:320px;height:434px;z-index:2;background:linear-gradient(to bottom left,#1f4d0e 0%,#3f7a14 24%,#5f9b1e 40%,#a8d62e 54%,rgba(168,214,46,0) 68%)}
.hero-title{position:absolute;left:0;width:1200px;text-align:center;color:var(--green-dark);font-weight:700;line-height:1}
.hero-title.l1{top:162px;font-size:52px}
.hero-title.l2{top:224px;font-size:44px}
.hero-sub{position:absolute;top:284px;width:1200px;text-align:center;font-size:13px;color:var(--muted)}
/* sections */
.section-title{position:absolute;left:0;width:1200px;text-align:center;font-size:26px;font-weight:600;color:var(--green-dark)}
.section-sub{position:absolute;left:0;width:1200px;text-align:center;font-size:10px;color:var(--muted)}
.intro{position:absolute;left:198px;top:704px;width:804px;text-align:center;font-size:10px;line-height:1.75;color:var(--muted)}
.statement{position:absolute;width:360px;font-size:9.5px;line-height:1.6;color:var(--muted)}
.statement h3{font-size:16px;font-weight:600;color:var(--text);margin-bottom:10px;display:flex;align-items:center;gap:8px}
.statement h3::before{content:"";width:10px;height:10px;border-radius:50%;background:var(--green-dark)}
.statement ul{list-style:none}
.statement li{padding-left:24px;position:relative}
.statement li::before{content:"";position:absolute;left:4px;top:7px;width:4px;height:4px;border-radius:50%;background:#333}
/* products */
.product{position:absolute;width:267px;height:188px;display:flex;align-items:center;justify-content:center;text-align:center;color:var(--white);font-size:18px;font-weight:600;line-height:1.4;padding:0 10px;text-shadow:0 1px 3px rgba(0,0,0,.35)}
/* testimonial */
.quote-mark{position:absolute;left:0;width:1200px;top:1612px;text-align:center;font-size:70px;font-weight:700;color:#bbb;line-height:1}
.quote-text{position:absolute;left:257px;top:1668px;width:686px;text-align:center;font-size:10px;line-height:1.8;color:var(--muted)}
.arrow-btn{position:absolute;top:1672px;width:24px;height:24px;background:#eee;display:flex;align-items:center;justify-content:center}
.author{position:absolute;left:0;width:1200px;top:1744px;text-align:center;font-size:16px;font-weight:600;color:var(--text)}
.author-role{position:absolute;left:0;width:1200px;top:1768px;text-align:center;font-size:13px;font-style:italic;color:#888}
/* news */
.news-panel{position:absolute;left:64px;top:1920px;width:1072px;height:390px;background:var(--grey-bg)}
.news-card{position:absolute;top:1950px;width:312px}
.news-img{width:312px;height:211px;position:relative}
.news-date{position:absolute;left:90px;bottom:0;width:134px;height:26px;background:var(--green-dark);color:var(--white);font-size:9px;display:flex;align-items:center;justify-content:center;gap:14px}
.news-title{font-size:12px;font-weight:600;margin-top:16px}
.news-text{font-size:9.5px;line-height:1.6;color:var(--muted);margin-top:8px}
.read-more{display:block;margin:14px auto 0;width:88px;height:25px;background:var(--green-dark);color:var(--white);font-size:8px;text-align:center;line-height:25px}
/* footer */
.footer-brand{position:absolute;left:496px;top:2388px;display:flex;align-items:center;gap:12px}
.footer-links{position:absolute;left:0;width:1200px;top:2468px;text-align:center;font-size:9.5px;color:#333}
.footer-head{position:absolute;top:2514px;font-size:25px;font-weight:600;color:var(--green-dark)}
.social{position:absolute;top:2562px;left:404px;display:flex;gap:18px}
.social span{width:26px;height:26px;border-radius:50%;background:var(--green-dark)}
.phone{position:absolute;left:626px;top:2556px;font-size:21px;letter-spacing:1.5px;color:#333}
</style>
</head>
<body>

<header class="site-header">
  <div class="brand"><span class="brand-dot"></span><span class="brand-name">Tillard Environmental Projects</span></div>
  <nav class="main-nav">
    <span>Home</span><span class="drop">About Us</span><span class="drop">Services</span><span class="drop">Products</span><span class="drop">News</span><span>Contact</span>
  </nav>
  <div class="search">Search
    <svg width="15" height="15" viewBox="0 0 15 15"><circle cx="6" cy="6" r="4.8" fill="none" stroke="#333" stroke-width="1.4"/><line x1="9.6" y1="9.6" x2="13.5" y2="13.5" stroke="#333" stroke-width="1.6"/></svg>
  </div>
</header>

<div class="hero-accent-right" role="img" aria-label="Decorative green swoosh in the top right corner"></div>

<section class="hero">
  <div class="hero-art" role="img" aria-label="Faint illustration of a tree growing over the globe"></div>
  <div class="hero-accent-left" role="img" aria-label="Decorative green swoosh in the lower left corner"></div>
  <div class="hero-title l1">World</div>
  <div class="hero-title l2">Environmental Day</div>
  <div class="hero-sub">Lorem Ipsum is simply Tillard Environmental Project</div>
</section>

<h2 class="section-title" style="top:632px">Who We Are</h2>
<div class="section-sub" style="top:668px">Lorem Ipsum is simply</div>
<p class="intro">Lorem Ipsum is simply dummy text of the printing and typesetting industry. Lorem Ipsum has been the industry's standard dummy text ever since the 1500s, when an unknown printer took a galley of type and scrambled it to make a type specimen book. It has survived not only five centuries, but also the leap into electronic typesetting, remaining essentially unchanged.</p>

<div class="statement" style="left:241px;top:790px;width:345px">
  <h3>Vision statement</h3>
  <p>Our Vision is to make it easy for everyone to minimise their environmental impact by providing information, technology, packaged green solutions &amp; helping innovation flourish.</p>
</div>
<div class="statement" style="left:610px;top:790px;width:370px">
  <h3>Mission Statement</h3>
  <p>Working with people to minimise the environmental impact of humans on the earth without sacrificing lifestyle and helping innovation flourish.</p>
  <p style="margin-top:10px">We will achieve this by focusing on the following:</p>
  <ul>
    <li>Sustainable food.</li>
    <li>Sustainable / Renewable power.</li>
    <li>Water quality &amp; treatment.</li>
    <li>Air quality.</li>
    <li>Investing in green infrastructure &amp; projects.</li>
  </ul>
</div>

<h2 class="section-title" style="top:994px">Our Product</h2>
<div class="section-sub" style="top:1030px">Lorem Ipsum is simply</div>

<div class="product" style="left:64px;top:1074px;background:linear-gradient(135deg,#8cbf3a,#4f8a1e)" role="img" aria-label="Photo of red berries on a green plant">Sustainable Food.</div>
<div class="product" style="left:332px;top:1074px;background:linear-gradient(180deg,#3e7a26,#6aa83a)" role="img" aria-label="Photo of a lawn with hedges">Green walls</div>
<div class="product" style="left:600px;top:1074px;background:linear-gradient(135deg,#4e7e26,#c9a98c)" role="img" aria-label="Photo of hands holding a seedling">Eco gardens</div>
<div class="product" style="left:868px;top:1074px;background:linear-gradient(135deg,#8a7a5c,#5f9b2e)" role="img" aria-label="Photo of a wicker chair beside a living plant wall">Living food walls</div>
<div class="product" style="left:198px;top:1282px;background:linear-gradient(135deg,#2b4a74,#8aa0b4)" role="img" aria-label="Photo of striped fish underwater">Aquaculture – Fish Farm– Barramundi</div>
<div class="product" style="left:466px;top:1282px;background:linear-gradient(135deg,#a6d45a,#5e9a24)" role="img" aria-label="Photo of a fresh lettuce head">Hydroponic gardens</div>
<div class="product" style="left:734px;top:1282px;background:linear-gradient(135deg,#c9a98a,#6b5a46)" role="img" aria-label="Photo of a seedling in soil on a trowel">Syndicated farms</div>

<h2 class="section-title" style="top:1522px">Our Testimonial</h2>
<div class="section-sub" style="top:1558px">Lorem Ipsum is simply</div>
<div class="quote-mark">“</div>
<div class="arrow-btn" style="left:125px"><svg width="8" height="10" viewBox="0 0 8 10"><path d="M6 1 L2 5 L6 9" fill="none" stroke="#333" stroke-width="1.6"/></svg></div>
<div class="arrow-btn" style="left:1050px"><svg width="8" height="10" viewBox="0 0 8 10"><path d="M2 1 L6 5 L2 9" fill="none" stroke="#333" stroke-width="1.6"/></svg></div>
<p class="quote-text">Lorem Ipsum is simply dummy text of the printing and typesetting industry. Lorem Ipsum has been the industry's standard dummy text ever since the 1500s, when an unknown printer took a galley of type and scrambled it to make a type specimen book. It has survived not only five centuries, but also the leap into electronic typesetting, remaining essentially unchanged.</p>
<div class="author">Dr. Lorem ipsum,</div>
<div class="author-role">Lorem Ipsum Is Simply Dummy,</div>

<h2 class="section-title" style="top:1840px">Our Lates News</h2>
<div class="section-sub" style="top:1876px">Lorem Ipsum is simply</div>
<div class="news-panel"></div>

<article class="news-card" style="left:94px">
  <div class="news-img" style="background:linear-gradient(180deg,#e8eee0,#6a9a3a)" role="img" aria-label="Photo of hands holding a young plant in soil">
    <div class="news-date"><span>◷ 2015/NOV/20</span><span>▭ 0</span></div>
  </div>
  <h3 class="news-title">Lorem Ipsum is simply</h3>
  <p class="news-text">Lorem Ipsum is simply dummy text of the printing and typesetting industry. Lorem Ipsum has been the industry's standard dummy</p>
  <span class="read-more">READ MORE</span>
</article>
<article class="news-card" style="left:459px">
  <div class="news-img" style="background:linear-gradient(180deg,#2f3a1a,#5a4230)" role="img" aria-label="Photo of a sprout growing from dark soil">
    <div class="news-date"><span>◷ 2015/NOV/20</span><span>▭ 0</span></div>
  </div>
  <h3 class="news-title">Lorem Ipsum is simply</h3>
  <p class="news-text">Lorem Ipsum is simply dummy text of the printing and typesetting industry. Lorem Ipsum has been the industry's standard dummy</p>
  <span class="read-more">READ MORE</span>
</article>
<article class="news-card" style="left:824px">
  <div class="news-img" style="background:linear-gradient(135deg,#6fa03e,#d9b9a0)" role="img" aria-label="Photo of cupped hands holding soil with a seedling">
    <div class="news-date"><span>◷ 2015/NOV/20</span><span>▭ 0</span></div>
  </div>
  <h3 class="news-title">Lorem Ipsum is simply</h3>
  <p class="news-text">Lorem Ipsum is simply dummy text of the printing and typesetting industry. Lorem Ipsum has been the industry's standard dummy</p>
  <span class="read-more">READ MORE</span>
</article>

<footer>
  <div class="footer-brand"><span class="brand-dot"></span><span class="brand-name">Tillard Environmental Projects</span></div>
  <div class="footer-links">Home | Abou Us | Privecy Policy | Account | Blog | Contact Us</div>
  <h3 class="footer-head" style="left:390px">Get In Touch</h3>
  <h3 class="footer-head" style="left:647px">Contact us</h3>
  <div class="social" aria-label="Social links"><span></span><span></span><span></span></div>
  <div class="phone">(123) 481 - 7362</div>
</footer>

</body>
</html>
```